Breezeway Comfort business cards design

Need a business card design for a Heating and Air Conditioning business. I need these items included.
Business name: Breezeway Comfort
Owner: Marcus Tollefsen
License # 2874590
Phone number # 555-382-4071
Email: breezewaycomfortair@mailvista.example
Sales
Service
Installation
Maintenance

Heating and Air Conditioning

Requirements
Must have
• Company name , license number , phone number , email

```html
<!DOCTYPE html>
<html lang="en">
<head>
<meta charset="utf-8">
<title>Breezeway Comfort – Business Cards</title>
<link href="https://fonts.googleapis.com/css2?family=Montserrat:wght@600;700&family=Arimo:wght@400&display=swap" rel="stylesheet">
<style>
  :root{
    --stage:#1c1d21;
    --blue-deep:#0a2a9c;
    --blue:#0d3ac2;
    --blue-light:#1445cf;
    --pattern-a:#0b32b0;
    --pattern-b:#1a4fd6;
    --orange:#f0761e;
    --pink:#e8265e;
    --white:#ffffff;
  }
  *{box-sizing:border-box;margin:0;padding:0}
  html,body{width:1200px;height:840px;overflow:hidden;background:var(--stage)}
  .canvas{position:relative;width:1200px;height:840px}
  .card{
    position:absolute;width:640px;height:366px;border-radius:26px;overflow:hidden;
    background:linear-gradient(135deg,var(--blue-deep),var(--blue) 55%,var(--blue-light));
    font-family:"Arimo",Arial,sans-serif;color:var(--white);
  }
  .card::after{
    content:"";position:absolute;left:0;right:0;bottom:0;height:4px;
    background:linear-gradient(90deg,var(--orange),var(--pink));
  }
  .card--back{left:60px;top:40px}
  .card--front{left:500px;top:434px}
  .pattern{
    position:absolute;inset:0;
    background:linear-gradient(120deg,var(--pattern-a),var(--pattern-b));
  }
  .brand{
    position:absolute;display:flex;align-items:center;gap:12px;
    font-family:"Montserrat",sans-serif;font-weight:700;color:var(--white);
    letter-spacing:.5px;white-space:nowrap;
  }
  .brand__dot{width:34px;height:34px;border-radius:50%;background:var(--orange);flex:none}
  .card--back .brand{left:50%;top:50%;transform:translate(-50%,-50%);font-size:30px}
  .card--front .brand{left:190px;top:62px;font-size:32px}
  .card--front .brand__dot{width:40px;height:40px}
  .person{position:absolute;left:110px;top:196px}
  .person__name{font-family:"Montserrat",sans-serif;font-weight:700;font-size:21px;letter-spacing:.5px}
  .person__role{font-size:16px;color:var(--orange);margin-top:2px}
  .divider{
    position:absolute;left:110px;top:256px;width:320px;height:3px;
    background:linear-gradient(90deg,var(--orange),var(--pink));
  }
  .license{
    position:absolute;left:418px;top:228px;width:200px;height:31px;
    background:linear-gradient(90deg,var(--pink),#e0204f);
    clip-path:polygon(0 0,100% 0,100% 100%,14% 100%);
    display:flex;align-items:center;justify-content:flex-end;padding-right:14px;
    font-size:15px;
  }
  .services{position:absolute;right:22px;top:272px;text-align:right;font-size:15px;line-height:1.5}
  .services .dot{display:inline-block;width:7px;height:7px;border-radius:50%;background:var(--orange);margin:0 4px 2px 8px}
  .contact{position:absolute;left:118px;top:286px;font-size:15px;line-height:1.7}
  .contact__row{display:flex;align-items:center;gap:8px}
  .contact__row svg{width:15px;height:15px;flex:none}
</style>
</head>
<body>
<main class="canvas">

  <section class="card card--back" aria-label="Card back">
    <div class="pattern" role="img" aria-label="Tone-on-tone repeating emblem pattern in blue"></div>
    <div class="brand"><span class="brand__dot"></span>Breezeway Comfort</div>
  </section>

  <section class="card card--front" aria-label="Card front">
    <div class="brand"><span class="brand__dot"></span>Breezeway Comfort</div>

    <div class="person">
      <p class="person__name">MARCUS TOLLEFSEN</p>
      <p class="person__role">Owner</p>
    </div>
    <div class="divider"></div>
    <div class="license">License # 2874590</div>

    <div class="services">
      <p><span class="dot"></span>Sales<span class="dot"></span>Service</p>
      <p><span class="dot"></span>Installation<span class="dot"></span>Maintenance</p>
    </div>

    <div class="contact">
      <p class="contact__row">
        <svg viewBox="0 0 24 24" aria-hidden="true"><path fill="#f0761e" d="M6.6 10.8a15 15 0 0 0 6.6 6.6l2.2-2.2a1 1 0 0 1 1-.25 11.4 11.4 0 0 0 3.6.57 1 1 0 0 1 1 1V20a1 1 0 0 1-1 1A17 17 0 0 1 3 4a1 1 0 0 1 1-1h3.5a1 1 0 0 1 1 1c0 1.25.2 2.45.57 3.57a1 1 0 0 1-.25 1z"/></svg>
        555-382-4071
      </p>
      <p class="contact__row">
        <svg viewBox="0 0 24 24" aria-hidden="true"><path fill="#f0761e" d="M3 5h18a1 1 0 0 1 1 1v12a1 1 0 0 1-1 1H3a1 1 0 0 1-1-1V6a1 1 0 0 1 1-1zm1 2.3V17h16V7.3l-8 5.2z"/></svg>
        breezewaycomfortair@mailvista.example
      </p>
    </div>
  </section>

</main>
</body>
</html>
```